Window Graphics for New Dental Office

This is a bank of windows along a busy street that a new dental office wants to cover in graphics. The file ideas for window designs is the look the client is going for. The template with bleed lines .pdf is a a 10 percent scaled version of the graphics for the graphic layout. The dental window placement diagram is a picture showing the actual windows that will be covered in light green and the other .pdf is the clients logo.

This dentist wants a high end botique look with an competent and inviting feel.

You may incorporate ideas like:
- Emergency and Same Day Appointments Available
- The lead dentist works with every patient
- latest technology for crowns and veneers in-house
- free teeth whitening kit with every expert consultation
- every patient is our best patient
- Financing available
- PPO insurance and Payment Plans Accepted

```html
<!DOCTYPE html>
<html lang="en">
<head>
<meta charset="utf-8">
<title>Summit Dental Studio – Window Graphics</title>
<link rel="stylesheet" href="https://fonts.googleapis.com/css2?family=Cabin:wght@400;500&display=swap">
<style>
  :root {
    --page: #ffffff;
    --header-band: #d9dadc;
    --glass: #c9cfdb;
    --glass-light: #d6dbe5;
    --brand-blue: #1f5aa6;
    --bubble-blue: #2a63c4;
    --bubble-sky: #4aa3e8;
    --bubble-navy: #3a3f8f;
    --line-white: #ffffff;
    --bleed-green: #2ecc2e;
    --trim-gray: #9a9a9a;
  }
  * { box-sizing: border-box; margin: 0; padding: 0; }
  html, body { width: 1200px; height: 642px; overflow: hidden; background: var(--page); }
  body { position: relative; font-family: "Cabin", sans-serif; }

  .window { position: absolute; top: 62px; height: 517px; }
  .window__header { position: absolute; left: 0; right: 0; top: 0; height: 136px; background: var(--header-band); }
  .window__glass { position: absolute; left: 0; right: 0; top: 136px; bottom: 0; background: var(--glass); }
  .window__sill { position: absolute; left: 0; right: 0; top: 416px; height: 2px; background: var(--line-white); opacity: .85; }
  .window--brand .window__glass { background: linear-gradient(180deg, var(--glass-light) 0%, #e4e8ef 45%, var(--glass) 100%); }

  .window--brand { left: 36px; width: 256px; }
  .window--urgent { left: 326px; width: 279px; }
  .window--lead { left: 610px; width: 274px; }
  .window--tech { left: 889px; width: 275px; }

  .bleed { position: absolute; top: 62px; height: 517px; width: 0; border-left: 2px dashed var(--bleed-green); }
  .bleed-top { position: absolute; top: 62px; height: 0; border-top: 2px dashed var(--bleed-green); }
  .trim-mark { position: absolute; left: 1162px; top: 38px; width: 8px; height: 578px; border: 1px solid var(--trim-gray); border-left: none; }

  .brand-name { position: absolute; left: 0; right: 0; top: 32px; text-align: center; color: var(--brand-blue); font-weight: 500; line-height: 1; }
  .brand-name__main { display: block; font-size: 40px; letter-spacing: 2px; }
  .brand-name__sub { display: block; font-size: 21px; letter-spacing: 1px; margin-top: 6px; }

  .art { position: absolute; }
  .art--hero { left: 45px; top: 110px; width: 162px; height: 170px; border-radius: 40% 40% 30% 30%;
    background: radial-gradient(ellipse at 50% 45%, #ffffff 0%, #cfe3f3 45%, rgba(214,219,229,0) 75%); }
  .art--network { left: 0; right: 0; top: 0; height: 85px;
    background: linear-gradient(180deg, rgba(255,255,255,.55) 0%, rgba(255,255,255,0) 100%); }
  .art--tooth { background: radial-gradient(ellipse at 50% 45%, rgba(255,255,255,.8) 0%, rgba(255,255,255,0) 72%); }

  .bubble { position: absolute; }
  .bubble svg { position: absolute; inset: 0; width: 100%; height: 100%; overflow: visible; }
  .bubble__text { position: absolute; color: var(--brand-blue); }

  .bubble--urgent { left: 50px; top: 110px; width: 191px; height: 162px; }
  .bubble--urgent .bubble__text { left: 26px; top: 42px; font-size: 19px; line-height: 1.4; }
  .bubble--lead { left: 54px; top: 69px; width: 195px; height: 170px; }
  .bubble--lead .bubble__text { left: 32px; top: 48px; font-size: 17px; line-height: 1.45; text-transform: uppercase; }
  .bubble--tech { left: 34px; top: 13px; width: 219px; height: 194px; }
  .bubble--tech .bubble__text { left: 30px; top: 40px; font-size: 13px; line-height: 2.05; letter-spacing: .5px; text-transform: uppercase; }
</style>
</head>
<body>
  <section class="window window--brand">
    <div class="window__header"></div>
    <div class="window__glass">
      <h1 class="brand-name"><span class="brand-name__main">SUMMIT</span><span class="brand-name__sub">DENTAL STUDIO</span></h1>
      <div class="art art--hero" role="img" aria-label="Glowing crystal-style tooth illustration"></div>
    </div>
    <div class="window__sill"></div>
  </section>

  <section class="window window--urgent">
    <div class="window__header"></div>
    <div class="window__glass">
      <div class="art art--network" role="img" aria-label="Fine white geometric line network"></div>
      <div class="bubble bubble--urgent">
        <svg viewBox="0 0 191 162" aria-hidden="true">
          <polygon points="6,8 182,2 188,148 112,152 98,166 90,152 10,156" fill="none" stroke="var(--line-white)" stroke-width="1.2" transform="rotate(-3 95 80)"/>
          <polygon points="10,6 184,10 180,150 108,150 96,164 88,150 4,146" fill="none" stroke="var(--bubble-sky)" stroke-width="1.5"/>
          <polygon points="14,12 178,6 186,142 104,146 92,160 84,148 8,152" fill="none" stroke="var(--bubble-blue)" stroke-width="1.2" transform="rotate(2 95 80)"/>
        </svg>
        <p class="bubble__text">Emergency and<br>Same Day<br>Appointments<br>Available</p>
      </div>
      <div class="art art--tooth" role="img" aria-label="White outline tooth icon" style="left:98px;top:288px;width:70px;height:65px;"></div>
    </div>
    <div class="window__sill"></div>
  </section>

  <section class="window window--lead">
    <div class="window__header"></div>
    <div class="window__glass">
      <div class="art art--network" role="img" aria-label="Fine white geometric line network"></div>
      <div class="bubble bubble--lead">
        <svg viewBox="0 0 195 170" aria-hidden="true">
          <polygon points="4,4 190,10 186,152 116,152 108,172 96,152 8,148" fill="none" stroke="var(--bubble-navy)" stroke-width="1.5"/>
          <polygon points="10,10 192,2 184,158 120,158 110,176 100,158 2,154" fill="none" stroke="var(--bubble-sky)" stroke-width="1.5" transform="rotate(-2 97 85)"/>
          <polygon points="14,2 180,14 190,146 110,150 100,166 92,150 12,158" fill="none" stroke="var(--line-white)" stroke-width="1.2"/>
        </svg>
        <p class="bubble__text">The lead<br>dentist<br>works with<br>every patient</p>
      </div>
      <div class="art art--tooth" role="img" aria-label="White outline tooth icon" style="left:148px;top:239px;width:97px;height:90px;"></div>
    </div>
    <div class="window__sill"></div>
  </section>

  <section class="window window--tech">
    <div class="window__header"></div>
    <div class="window__glass">
      <div class="bubble bubble--tech">
        <svg viewBox="0 0 219 194" aria-hidden="true">
          <polygon points="2,12 214,2 206,176 126,172 112,194 104,170 10,170" fill="none" stroke="var(--line-white)" stroke-width="1.2" transform="rotate(-4 110 95)"/>
          <polygon points="6,20 210,8 214,168 122,168 110,190 100,166 4,176" fill="none" stroke="var(--bubble-navy)" stroke-width="1.5"/>
          <polygon points="10,26 216,14 208,172 118,176 106,194 96,174 14,168" fill="none" stroke="var(--bubble-blue)" stroke-width="1.5" transform="rotate(2 110 95)"/>
          <polygon points="14,32 212,22 204,180 114,180 102,196 94,178 8,174" fill="none" stroke="var(--bubble-sky)" stroke-width="1.3"/>
        </svg>
        <p class="bubble__text">Latest technology<br>for crowns<br>and veneers<br>in-house</p>
      </div>
      <div class="art art--tooth" role="img" aria-label="White outline tooth icon" style="left:59px;top:231px;width:129px;height:114px;"></div>
    </div>
    <div class="window__sill"></div>
  </section>

  <div class="bleed-top" style="left:36px;width:256px;"></div>
  <div class="bleed-top" style="left:326px;width:838px;"></div>
  <div class="bleed" style="left:35px;"></div>
  <div class="bleed" style="left:291px;"></div>
  <div class="bleed" style="left:325px;"></div>
  <div class="bleed" style="left:607px;"></div>
  <div class="bleed" style="left:886px;"></div>
  <div class="bleed" style="left:1163px;"></div>
  <div class="trim-mark"></div>
</body>
</html>
```